Peachynova.com adult webpage with links to various sites she is on.

UPDATE 3/10- let’s keep this a bit more simple. I am uploading three pics and a sketch of how she wants her site to look. It’s really just a page that has her links.

Looking to set up a homepage for my hot wife that has her clickable links on there. Pehaps a space for an about me and some notes encouraging audience to click and join velvet door.
Paqora link:

https://velvetdoorclub.com/away?url=https://Paqora.com/peachynova

Here is some
Copy from her:
“Queen of Dirty Talk” is important to work in.
🔥HOTWIFE SUPER SLUT🔥

...... I do things the other girls don’t! I suck and fuck like no other woman you’ll ever see. Filthy dirty talk, lots of sloppy oral, fantasy role play, dress up and cum swallowing.

Cum watch me! Have your mind..... and your big fat load blown away!

💋This page is where you will find ALL my links. My free velvetdoor has my videos for sale. My VIP page you will get the same videos at a discounted prices, plus lots of juicy extras. I also answer all my messages there. Make sure to check out my VIP page today so you don’t miss out on any of the fun!💋💋💋
Updates

I am tryin go to extend the project time to at least two weeks. I just don’t know how to edit. I have an email out to support.

Target Market(s)

Adult entertainment

Industry/Entity Type

Porn

Coding

Coded - Design and coding required

Number of Pages Required

1 page

Colors
000000
eea4c8

Requirements
Must have
• PeachyNova (no space between) is her stage name.
She would like maybe some cute horns in the logo. Maybe make the “S” have little devil horns on top and roll the bottom of the “S” like a devil tail with the arrows/spade point at at end.
A hot pic of her in background.
Buttons to her various pages.
Nice to have
• Perhaps an about me drop down or window we can write copy for? Pink black and leopard are good color choices.

```html
<!DOCTYPE html>
<html lang="en">
<head>
<meta charset="utf-8">
<title>PeachyNova – Queen of Dirty Talk</title>
<link rel="stylesheet" href="https://fonts.googleapis.com/css2?family=Figtree:wght@400;500&family=Montserrat:wght@400;500;700&family=Great+Vibes&display=swap">
<style>
  :root {
    --black: #000000;
    --footer: #0c0c0c;
    --pink: #eea4c8;
    --pink-deep: #e387b6;
    --white: #ffffff;
    --body-text: #b9b9b9;
    --muted: #a8a8a8;
  }
  * { box-sizing: border-box; margin: 0; padding: 0; }
  html, body { width: 952px; height: 1200px; overflow: hidden; background: var(--black); }
  body { font-family: "Montserrat", sans-serif; color: var(--white); position: relative; }

  .site-header { position: absolute; left: 0; top: 0; width: 952px; height: 81px; background: var(--black); }
  .site-title { position: absolute; left: 122px; top: 22px; display: flex; align-items: center; gap: 10px;
    font-family: "Figtree", sans-serif; font-weight: 400; font-size: 32px; line-height: 1; color: var(--white); }
  .site-title .accent { color: var(--pink); }
  .site-title .mark { width: 28px; height: 28px; border-radius: 50%; border: 2px solid var(--pink); }
  .contact { position: absolute; left: 550px; top: 34px; display: flex; align-items: center; gap: 6px;
    font-family: "Figtree", sans-serif; }
  .contact .label { font-size: 12.5px; color: var(--pink); }
  .contact .email { font-size: 16px; color: var(--white); }

  .hero { position: absolute; left: 0; top: 81px; width: 952px; height: 404px; overflow: hidden;
    background: linear-gradient(160deg, #d9d9d9 0%, #8a8a8a 35%, #3e3e3e 60%, #6f6f6f 85%, #4a4a4a 100%); }
  .hero-name { position: absolute; left: 116px; top: 317px; font-family: "Montserrat", sans-serif;
    font-weight: 400; font-size: 68px; line-height: 68px; color: var(--white); letter-spacing: -0.5px;
    text-shadow: 0 2px 6px rgba(0,0,0,0.35); white-space: nowrap; }

  .portrait-ring { position: absolute; left: 96px; top: 578px; width: 362px; height: 362px; border-radius: 50%;
    border: 10px solid var(--pink); background: radial-gradient(circle at 45% 45%, #e6e6e6 0%, #a4a4a4 55%, #4d4d4d 100%); }

  .about { position: absolute; left: 497px; top: 556px; width: 345px; }
  .about-title { font-family: "Great Vibes", cursive; font-weight: 400; font-size: 46px; color: var(--white); line-height: 1; }
  .about-copy { margin-top: 12px; font-size: 13.4px; line-height: 18.4px; color: var(--body-text); }
  .about-copy + .about-copy { margin-top: 9px; }

  .links-heading { position: absolute; left: 497px; top: 754px; font-size: 18px; font-weight: 400; color: var(--white); }
  .link-card { position: absolute; left: 499px; width: 341px; height: 40px; border: 1.5px solid var(--pink);
    display: flex; align-items: center; text-decoration: none; }
  .link-card .icon { width: 52px; display: flex; justify-content: center; align-items: center; flex-shrink: 0; }
  .link-card .text { display: flex; flex-direction: column; white-space: nowrap; }
  .link-card .name { font-size: 10.5px; font-weight: 700; color: var(--pink); letter-spacing: 0.1px; }
  .link-card .url { font-size: 9px; color: var(--white); text-decoration: underline; margin-top: 1px; }
  .link-card.is-vip { background: linear-gradient(90deg, var(--pink-deep), #f3bcd8); border-color: var(--pink);
    box-shadow: 0 0 8px rgba(238,164,200,0.35); }
  .link-card.is-vip .name, .link-card.is-vip .url { color: var(--black); }
  .plain-dot { width: 20px; height: 20px; border-radius: 50%; background: var(--pink); }
  .plain-square { width: 20px; height: 20px; border-radius: 3px; background: var(--pink); }

  .site-footer { position: absolute; left: 0; top: 1095px; width: 952px; height: 105px; background: var(--footer); }
  .copyright { position: absolute; left: 0; width: 952px; top: 27px; text-align: center; font-size: 9.5px; color: var(--muted); }
  .social { position: absolute; top: 55px; left: 411px; display: flex; gap: 5px; }
  .social span { width: 27px; height: 27px; border-radius: 50%; background: var(--pink); display: block; }
</style>
</head>
<body>
  <header class="site-header">
    <div class="site-title"><span class="mark"></span><span>Queen of <span class="accent">Dirty Talk</span></span></div>
    <div class="contact">
      <svg width="20" height="15" viewBox="0 0 20 15" aria-hidden="true">
        <rect x="0.75" y="0.75" width="18.5" height="13.5" fill="none" stroke="#fff" stroke-width="1.3"/>
        <path d="M1 1 L10 8.5 L19 1 M1 14 L7.5 7 M19 14 L12.5 7" fill="none" stroke="#fff" stroke-width="1.3"/>
      </svg>
      <span class="label">Contact me:</span>
      <span class="email">Peachynovaxxx@mailbloom.net</span>
    </div>
  </header>

  <section class="hero" role="img" aria-label="Black and white boudoir photo of PeachyNova lying on a bed in lingerie and stockings">
    <div class="hero-name">PeachyNova</div>
  </section>

  <div class="portrait-ring" role="img" aria-label="Black and white close-up portrait of PeachyNova in a pink circular frame"></div>

  <section class="about">
    <h2 class="about-title">About Me</h2>
    <p class="about-copy">I do things the other girls don’t! I suck and fuck like no other woman you’ll ever see. Filthy dirty talk, lots of sloppy oral, fantasy role play, dress up and cum swallowing.</p>
    <p class="about-copy">Cum watch me! Have your mind..... and your big fat load blown away!</p>
  </section>

  <h3 class="links-heading">Links</h3>

  <a class="link-card" style="top:788px" href="#">
    <span class="icon"><span class="plain-dot"></span></span>
    <span class="text"><span class="name">FREE VELVETDOOR</span><span class="url">www.velvetdoorclub.com/peachynova</span></span>
  </a>
  <a class="link-card is-vip" style="top:838px" href="#">
    <span class="icon">
      <svg width="22" height="26" viewBox="0 0 22 26" aria-hidden="true">
        <path d="M5 11 V7 a6 6 0 0 1 12 0 V11" fill="none" stroke="#000" stroke-width="3"/>
        <rect x="1" y="10" width="20" height="15" rx="4" fill="#000"/>
        <circle cx="11" cy="16" r="2.4" fill="#eea4c8"/>
        <rect x="10" y="17" width="2" height="4" fill="#eea4c8"/>
      </svg>
    </span>
    <span class="text"><span class="name">VIP VELVETDOOR</span><span class="url">www.velvetdoorclub.com/peachynovavip</span></span>
  </a>
  <a class="link-card" style="top:888px" href="#">
    <span class="icon"><span class="plain-square"></span></span>
    <span class="text"><span class="name">CLIPHAVEN</span><span class="url">https://cliphaven.com/channel/UCkR7mTqPzLw3Hn8YdXbEa_v</span></span>
  </a>
  <a class="link-card" style="top:938px" href="#">
    <span class="icon"><span class="plain-dot"></span></span>
    <span class="text"><span class="name">PAQORA</span><span class="url">https://paqora.com/code?user_id=5820391746602937158</span></span>
  </a>
  <a class="link-card" style="top:987px" href="#">
    <span class="icon"><span class="plain-square"></span></span>
    <span class="text"><span class="name">PICTURELY</span><span class="url">https://picturely.com/peachynova4?r=nametag</span></span>
  </a>

  <footer class="site-footer">
    <p class="copyright">Copyright © 2020-2021 Peachynova |&nbsp; Privacy | Terms</p>
    <div class="social">
      <span aria-label="Friendloop"></span>
      <span aria-label="Reelmark"></span>
      <span aria-label="ClipHaven"></span>
      <span aria-label="Picturely"></span>
    </div>
  </footer>
</body>
</html>
```